Mobile App UI for Telecommunications/Hosting Company

We are about to convert our existing self-service Customer Portal into a mobile phone application and need an elegant and professional UI/UX design. Our company provides telecommunication (voice/mobile/data) and hosting services to medium-sized business. The primary purpose of the application is to view trouble tickets, alerts, orders, and performance charts. This application is available to customers only - not the general public.

Please provide a UI design suitable for display on iPhone/Android devices. The attached document includes a proposed screen flow. You are free to design your own screens to display the same information elegantly.
Updates

Please note that the design should be based on the wireframes in the Word document, not the screenshots.  The screenshots are just to show our existing web portal look & feel.

Also, just a few screens are required for initial submission (3 would be great).

Thanks,
Dermot.

Target Market(s)

IT Managers away from their desk and using a mobile phone application.
Adult males from technical background aged 30-50.
Customers of Brindlewood Networks have access to this application (not the general public). This is a self-service portal for customers only.

Industry/Entity Type

Business

Colors
0592cd
33a6d7
85cae6
cadf82
fde08a

Requirements
Must have
• Please look at the screenshots from our current Customer Portal site (part of the project brief). The mobile app does not have to look the same, but should follow a similar style.

Please check out our company web site at www.brindlewoodnetworks.example (this site is not the customer portal and has a different look at feel) to understand what Brindlewood Networks does.
Nice to have
• Sharing capabilities via email/SMS.
A nice background image to make it stand out
The colours selected below are a guide only as they are similar to the corporate colours
- The priority is something that works on a phone - a design extendable to tablets is a nice to have as our existing web site looks OK on a tablet..

```html
<!DOCTYPE html>
<html lang="en">
<head>
<meta charset="utf-8">
<title>Sign In</title>
<link rel="stylesheet" href="https://fonts.googleapis.com/css2?family=Open+Sans:wght@400;600;700&display=swap">
<style>
  :root {
    --sky-top: #0b63c0;
    --sky-mid: #0a4a98;
    --deep-blue: #082c63;
    --glass-cyan: #3c9fd0;
    --field-bg: #3a3e45;
    --icon-cell: #2f3237;
    --icon-grey: #a3a6aa;
    --placeholder: #c3c5c8;
    --accent: #33a6d7;
    --white: #ffffff;
    --muted: #a9aeb4;
  }
  * { box-sizing: border-box; margin: 0; padding: 0; }
  html, body { width: 676px; height: 1200px; overflow: hidden; }
  body { font-family: "Open Sans", "Segoe UI", sans-serif; background: var(--deep-blue); }

  .screen { position: relative; width: 676px; height: 1200px; overflow: hidden; }

  .backdrop {
    position: absolute; inset: 0;
    background:
      radial-gradient(ellipse 260px 420px at 60px 820px, rgba(60,159,208,0.55), transparent 70%),
      radial-gradient(ellipse 300px 260px at 430px 1120px, rgba(120,190,225,0.45), transparent 70%),
      radial-gradient(ellipse 240px 520px at 420px 560px, rgba(40,120,200,0.35), transparent 70%),
      linear-gradient(180deg, var(--sky-top) 0%, var(--sky-mid) 35%, var(--deep-blue) 70%, #0b3f78 100%);
  }

  .login { position: absolute; left: 110px; top: 441px; width: 480px; }

  .field { display: flex; height: 80px; background: var(--field-bg); margin-bottom: 26px; }
  .field-icon {
    width: 81px; height: 80px; background: var(--icon-cell);
    display: flex; align-items: center; justify-content: center;
  }
  .field-label {
    padding-left: 27px; display: flex; align-items: center;
    font-size: 29px; color: var(--placeholder); font-weight: 400;
  }

  .sign-in {
    display: flex; align-items: center; justify-content: center;
    margin-top: 42px; height: 80px; background: var(--accent);
    color: var(--white); font-weight: 700; font-size: 33px; letter-spacing: 0.5px;
    text-shadow: 0 2px 3px rgba(0,0,0,0.45);
  }

  .sign-up {
    margin-top: 22px; display: flex; align-items: center; justify-content: center;
    font-size: 23px; gap: 8px; padding-left: 20px;
  }
  .sign-up-prompt { color: var(--muted); }
  .sign-up-link { color: var(--white); }
  .sign-up-arrow { margin-left: 8px; }
</style>
</head>
<body>
<main class="screen">
  <div class="backdrop" role="img" aria-label="Photo of a modern blue glass office building entrance with a man climbing carpeted steps, overlaid with fine flowing light lines"></div>

  <form class="login">
    <div class="field">
      <span class="field-icon">
        <svg width="46" height="46" viewBox="0 0 46 46" aria-hidden="true">
          <ellipse cx="23" cy="15" rx="10" ry="12" fill="var(--icon-grey)"/>
          <path d="M2 44 C4 32 12 29 18 28 L23 34 L28 28 C34 29 42 32 44 44 Z" fill="var(--icon-grey)"/>
        </svg>
      </span>
      <span class="field-label">username</span>
    </div>
    <div class="field">
      <span class="field-icon">
        <svg width="38" height="48" viewBox="0 0 38 48" aria-hidden="true">
          <path d="M9 22 V14 a10 10 0 0 1 20 0 V22" fill="none" stroke="var(--icon-grey)" stroke-width="5"/>
          <rect x="2" y="20" width="34" height="27" rx="5" fill="var(--icon-grey)"/>
          <circle cx="19" cy="31" r="4" fill="var(--icon-cell)"/>
          <rect x="17" y="32" width="4" height="8" fill="var(--icon-cell)"/>
        </svg>
      </span>
      <span class="field-label">password</span>
    </div>

    <div class="sign-in">SIGN IN</div>

    <p class="sign-up">
      <span class="sign-up-prompt">Not a member?</span>
      <span class="sign-up-link">Sign up now</span>
      <svg class="sign-up-arrow" width="38" height="24" viewBox="0 0 38 24" aria-hidden="true">
        <path d="M0 9 H22 V2 L37 12 L22 22 V15 H0 Z" fill="var(--white)"/>
      </svg>
    </p>
  </form>
</main>
</body>
</html>
```